Webdesign for a Bikeshop in Innsbruck (male audience)

To obtain my master's degree, I am conducting a study in the field of web design as part of my master thesis. All submitted designs will therefore be used for study purposes. In order to achieve a homogeneous group, I would like to encourage not only male but also female web designers to submit a design. All submitted designs will be used anonymously for the study and therefore do not allow any conclusions to be drawn about your person. Since this is a contest, the winner will be chosen randomly from all serious submissions. I would be really happy if you would support me in my study. I think the results could be very informative and also useful for your further work (I won't go into more detail here as it could skew the results - but once the contest is over, feel free to contact me. Of course I will also provide you with my results as soon as my work is finished). Below you will find a fictitious usecase and a description of what the website should include:

The company Veloria Kastwerk is planning to relaunch its own website and would like to present itself primarily as a competent and leading consultant in the field of cargo bikes. The design should appeal to a broad audience and embody an urban lifestyle. In any case, the website should include a landing page, a product overview page and a product details page. The company also wants to appeal mainly to a MALE target group. You only design the website. So don't worry about hardware or software limitations, just create the best bike store design you can.

As it is fictitious, I can't offer any materials. A logo is not necessary, you can use a placeholder or whatever you have access to. If you need any inspring websites feel free to contact me.

Target Market(s)

male users

Number of Pages Required

1 page

Requirements
Must have
• landing page, product overview page, product details page
Should not have
• online shop

```html
<!DOCTYPE html>
<html lang="en">
<head>
<meta charset="utf-8">
<title>Veloria Kastwerk – Cargo Bikes</title>
<link rel="stylesheet" href="https://fonts.googleapis.com/css2?family=Roboto+Condensed:wght@400;700&family=Roboto:wght@400;500;700&display=swap">
<style>
:root{
  --orange:#f47a20;
  --orange-deep:#ee6417;
  --orange-soft:#f98a3a;
  --blue:#2d67a0;
  --blue-deep:#24598f;
  --ink:#1b1b1b;
  --text:#444;
  --muted:#666;
  --card:#f3f3f3;
  --dark:#141414;
  --white:#fff;
}
*{box-sizing:border-box;margin:0;padding:0}
html,body{width:1200px;height:4231px;overflow:hidden}
body{font-family:"Roboto",sans-serif;color:var(--text);background:var(--white);position:relative}
.abs{position:absolute}
h1,h2,h3,.cond{font-family:"Roboto Condensed",sans-serif}
.accent{color:var(--orange)}
.btn{display:inline-flex;align-items:center;gap:10px;background:var(--orange);color:#fff;font-weight:700;font-size:14px;text-transform:uppercase;letter-spacing:.3px;padding:0 28px;height:50px;text-decoration:none}
.btn .dot{width:14px;height:14px;border-radius:50%;background:#fff;display:inline-flex;align-items:center;justify-content:center}
.btn .dot svg{width:8px;height:8px}

/* header */
.topbar{top:0;left:0;width:1200px;height:120px}
.topbar .contact{display:flex;align-items:center;gap:14px;top:22px}
.topbar .contact small{display:block;font-size:12px;color:#333}
.topbar .contact b{font-size:14px;color:#111;font-weight:500}
.brand{font-family:"Roboto Condensed",sans-serif;font-weight:700;font-size:36px;color:var(--ink);left:0;width:1200px;text-align:center;top:20px}
.nav{top:92px;left:112px;width:976px;height:62px;background:var(--orange);display:flex;align-items:center;z-index:3}
.nav a{color:#fff;text-decoration:none;font-size:14px;text-transform:uppercase}
.nav .home{background:var(--orange-deep);height:62px;width:112px;display:flex;align-items:center;justify-content:center;font-weight:700}
.nav .links{display:flex;gap:0;margin-left:12px}
.nav .links a{padding:0 12px}
.nav .links span{color:#fff;opacity:.8}
.nav .quote{margin-left:auto;background:var(--orange-deep);height:62px;width:190px;display:flex;align-items:center;justify-content:center;gap:10px;font-weight:700}

/* hero */
.hero{top:120px;left:0;width:1200px;height:720px}
.hero .photo{position:absolute;inset:0;background:linear-gradient(100deg,#2c2a26 0%,#4a4237 35%,#6b6252 60%,#8d8a6e 80%,#b6b39a 100%)}
.hero .copy{left:110px;top:190px;color:#fff}
.hero .copy h3{font-size:34px;font-weight:700}
.hero .copy h1{font-size:56px;font-weight:700;line-height:1.1;margin-top:6px}
.hero .copy p{font-size:15px;line-height:26px;width:420px;margin-top:14px}
.hero .copy .btn{margin-top:26px;height:50px;padding:0 28px}

/* section heads */
.sec-title{left:0;width:1200px;text-align:center;font-size:36px;font-weight:700;color:var(--ink)}

/* products */
.product{width:231px}
.product .img{height:196px;background:var(--card);border-radius:8px}
.product h4{font-size:16px;font-weight:700;color:#111;margin-top:26px}
.product p{font-size:15px;line-height:26px;color:#333;margin-top:8px}

/* about */
.about{top:1364px;left:0;width:1200px;height:603px;background:linear-gradient(90deg,var(--blue-deep),var(--blue) 60%,#3470aa)}
.about .ring{left:112px;top:80px;width:444px;height:444px;border-radius:50%;border:4px solid var(--orange);padding:6px}
.about .ring div{width:100%;height:100%;border-radius:50%;background:linear-gradient(160deg,#7a8a52,#a08b62 55%,#5a5244)}
.about h2{left:606px;top:104px;font-size:36px;color:#fff;font-weight:700}
.about p{left:606px;top:166px;width:482px;font-size:15px;line-height:25.6px;color:#fff;text-align:justify}
.about .btn{left:606px;top:447px;height:52px;padding:0 28px}

/* how it works */
.step{width:336px;text-align:center;height:368px;top:2134px;padding-top:23px}
.step.active{background:#fff;border-radius:26px;box-shadow:0 4px 28px rgba(0,0,0,.14);border-bottom:4px solid var(--orange)}
.step .icon{width:114px;height:114px;border-radius:50%;background:var(--orange);margin:0 auto;display:flex;align-items:center;justify-content:center}
.step h3{font-family:"Roboto",sans-serif;font-size:18px;font-weight:700;color:#111;margin-top:36px}
.step p{font-size:14px;line-height:24px;color:#555;width:290px;margin:14px auto 0}
.step .more{display:inline-flex;align-items:center;gap:8px;color:var(--orange);font-size:13px;font-weight:700;margin-top:28px}
.step .more i{width:13px;height:13px;border-radius:50%;background:var(--orange);display:inline-block}

/* testimonials */
.testi{top:2597px;left:0;width:1200px;height:547px;background:linear-gradient(90deg,var(--orange-soft),#f8913f 50%,var(--orange))}
.testi h2{top:80px;left:0;width:1200px;text-align:center;color:#fff;font-size:36px;font-weight:700}
.testi .lead{top:137px;left:190px;width:820px;text-align:center;color:#fff;font-size:15px;line-height:26px}
.quote-card{top:236px;width:314px;height:224px;background:#fff;padding:30px 22px 0}
.quote-card p{font-size:14px;line-height:25px;color:#666;text-align:justify}
.quote-card .who{display:flex;align-items:center;margin-top:22px;gap:14px}
.quote-card .avatar{width:52px;height:52px;border-radius:50%;background:linear-gradient(160deg,#c9b8a2,#8b7460)}
.quote-card .who b{font-size:15px;color:#111;display:block}
.quote-card .stars{color:var(--orange);font-size:12px;letter-spacing:1px}
.quote-card .mark{margin-left:auto;font-family:"Roboto Condensed",sans-serif;color:var(--orange);font-size:72px;font-weight:700;line-height:1;height:40px;transform:translateY(6px)}

/* gallery */
.tile{border-radius:2px}

/* footer */
.footer{top:3740px;left:0;width:1200px;height:491px}
.footer .brandf{left:108px;top:140px;font-family:"Roboto Condensed",sans-serif;font-size:34px;font-weight:700;color:#fff}
.footer .about-f{left:110px;top:194px;width:260px;font-size:14px;line-height:24px;color:#ddd}
.footer .social{left:110px;top:282px;display:flex;gap:7px}
.footer .social span{width:32px;height:32px;border-radius:50%;border:1px solid #fff;display:block}
.footer h5{font-size:16px;font-weight:500;color:#fff;margin-bottom:12px}
.footer ul{list-style:none}
.footer li{font-size:15px;line-height:30px;color:#eee}
.footer .ci{display:flex;gap:14px;margin-bottom:14px}
.footer .ci small{display:block;font-size:12px;font-weight:700;color:#fff}
.footer .ci span{font-size:14px;line-height:22px;color:#eee}
.footer .rule{left:110px;top:395px;width:980px;height:1px;background:#444}
.footer .copy{left:0;width:1200px;top:424px;text-align:center;color:#fff;font-size:14px}
.footer .up{left:1137px;top:360px;width:36px;height:36px;border-radius:50%;background:var(--orange);display:flex;align-items:center;justify-content:center}
</style>
</head>
<body>

<!-- header -->
<header class="abs topbar">
  <div class="abs contact" style="left:112px">
    <svg width="30" height="26" viewBox="0 0 30 26"><rect x="1" y="5" width="28" height="19" rx="2" fill="none" stroke="#f47a20" stroke-width="2.4"/><path d="M2 7l13 9 13-9" fill="none" stroke="#f47a20" stroke-width="2.4"/></svg>
    <div><small>Email Us</small><b>info@veloriakastwerk.com</b></div>
  </div>
  <div class="abs brand">Veloria Kastwerk</div>
  <div class="abs contact" style="left:926px">
    <svg width="28" height="28" viewBox="0 0 24 24"><path d="M6.6 10.8c1.4 2.8 3.8 5.1 6.6 6.6l2.2-2.2c.3-.3.7-.4 1-.2 1.1.4 2.3.6 3.6.6.6 0 1 .4 1 1V20c0 .6-.4 1-1 1C10.6 21 3 13.4 3 4c0-.6.4-1 1-1h3.5c.6 0 1 .4 1 1 0 1.3.2 2.5.6 3.6.1.3 0 .7-.2 1z" fill="#f47a20"/></svg>
    <div><small>Call or text us</small><b>+1 555 014 2299</b></div>
  </div>
</header>

<nav class="abs nav">
  <a class="home" href="#">Home</a>
  <div class="links">
    <a href="#">About Us</a><span>|</span>
    <a href="#">Products</a><span>|</span>
    <a href="#">Services</a><span>|</span>
    <a href="#">Blog</a><span>|</span>
    <a href="#">Contact Us</a>
  </div>
  <a class="quote" href="#">Get a Quote
    <svg width="14" height="14" viewBox="0 0 14 14"><circle cx="7" cy="7" r="7" fill="#fff"/><path d="M5 4l3 3-3 3" stroke="#ee6417" stroke-width="2" fill="none"/></svg>
  </a>
</nav>

<!-- hero -->
<section class="abs hero">
  <div class="photo" role="img" aria-label="Courier riding a yellow cargo bike loaded with parcels down a city street"></div>
  <svg class="abs" style="left:0;top:560px" width="1200" height="160" viewBox="0 0 1200 160">
    <path d="M0 40 C300 150 800 150 1200 40 L1200 160 L0 160Z" fill="#fff"/>
    <path d="M0 40 C300 150 800 150 1200 40 L1200 48 C800 158 300 158 0 48Z" fill="#f47a20"/>
    <path d="M0 40 C300 150 800 150 1200 40" fill="none" stroke="#f47a20" stroke-width="4"/>
  </svg>
  <div class="abs copy">
    <h3>Welcome To</h3>
    <h1>Veloria Kastwerk</h1>
    <p>Lorem ipsum dolor sit amet consectetur adipiscing elit sed do eiusmod tempor incididunt ut labore dolored magnad.</p>
    <a class="btn" href="#">Get Started <span class="dot"><svg viewBox="0 0 8 8"><path d="M2 1l3 3-3 3" stroke="#f47a20" stroke-width="1.6" fill="none"/></svg></span></a>
  </div>
</section>

<!-- products -->
<h2 class="abs sec-title" style="top:910px">Our <span class="accent">Products</span></h2>
<div class="abs product" style="left:112px;top:987px"><div class="img" role="img" aria-label="Orange city bike with front basket"></div><h4>Products Tittle</h4><p>Lorem ipsum dolor consectetur adipiscing elited sed eiusmod.</p></div>
<div class="abs product" style="left:360px;top:987px"><div class="img" role="img" aria-label="Long-tail cargo bike with yellow box"></div><h4>Products Tittle</h4><p>Lorem ipsum dolor consectetur adipiscing elited sed eiusmod.</p></div>
<div class="abs product" style="left:609px;top:987px"><div class="img" role="img" aria-label="Front-loader cargo bike with red box"></div><h4>Products Tittle</h4><p>Lorem ipsum dolor consectetur adipiscing elited sed eiusmod.</p></div>
<div class="abs product" style="left:857px;top:987px"><div class="img" role="img" aria-label="Electric cargo bike with orange tub"></div><h4>Products Tittle</h4><p>Lorem ipsum dolor consectetur adipiscing elited sed eiusmod.</p></div>

<!-- about -->
<section class="abs about">
  <div class="abs ring"><div role="img" aria-label="Rider with backpack on a cargo bike carrying boxes in a park"></div></div>
  <h2 class="abs">About Veloria Kastwerk</h2>
  <p class="abs">Lorem ipsum dolor sited ameted consectetur adipiscing elit sed do eiusmod tempor incididunt ut labore et dolore magna aliquad Ut enim ad minim veniam, quis nostrud exercitation ullamtcod laboris nisi ut aliquip exntea bhcommodo consequated Duis auted irure dolor in reprehenderit in voluptate velited esse cillegbum dolore euwsdf fugiat nulla pariatur Excepteur sint occaecated cupidatat non proident sunt in culpa qui officia deserunt mollit anim id ested laborumLorem ipsum dolor sit ameted consectetur adipiscing elited sed do eiusmod tempor incididunt laborumLorem ipsum dolor sit amet consectetur dolore magna minim veniam quis nostrudExcepteur sinted exercitation.</p>
  <a class="abs btn" href="#">Learn More <span class="dot"><svg viewBox="0 0 8 8"><path d="M2 1l3 3-3 3" stroke="#f47a20" stroke-width="1.6" fill="none"/></svg></span></a>
</section>

<!-- how it works -->
<h2 class="abs sec-title" style="top:2044px">How it <span class="accent">Work</span></h2>
<div class="abs step" style="left:91px">
  <div class="icon"><svg width="70" height="50" viewBox="0 0 70 50" fill="none" stroke="#fff" stroke-width="3"><circle cx="14" cy="34" r="11"/><circle cx="56" cy="34" r="11"/><path d="M14 34l12-18h20l10 18M26 16l9 18h-21M35 34l11-18M22 10h8M44 10h6"/></svg></div>
  <h3>Lorem ipsum dolor sit a</h3>
  <p>We design bottles in cooperation with clients or on our own. When designing, we follow technical requirements, suggestions from the customer and our own</p>
  <span class="more">READ MORE <i></i></span>
</div>
<div class="abs step active" style="left:440px">
  <div class="icon"><svg width="70" height="54" viewBox="0 0 70 54" fill="none" stroke="#fff" stroke-width="3"><circle cx="14" cy="40" r="10"/><circle cx="56" cy="40" r="10"/><rect x="6" y="18" width="26" height="14"/><path d="M32 32l12-16h8l4 24M44 16l-4-8h8"/></svg></div>
  <h3>Lorem ipsum dolor sit a</h3>
  <p>We make blow bottles based on our projects and those provided by customers. We are able to produce 8 million bottles of one design per month.</p>
  <span class="more">READ MORE <i></i></span>
</div>
<div class="abs step" style="left:786px">
  <div class="icon"><svg width="70" height="56" viewBox="0 0 70 56" fill="none" stroke="#fff" stroke-width="3"><circle cx="16" cy="12" r="6"/><path d="M38 14a8 8 0 0 1 15 2h2a5 5 0 0 1 0 10H38a6 6 0 0 1 0-12z"/><circle cx="14" cy="42" r="10"/><circle cx="56" cy="42" r="10"/><path d="M14 42l12-14h18l12 14M30 28l8 14"/></svg></div>
  <h3>Lorem ipsum dolor sit a</h3>
  <p>We produce PET bottles with a capacity of 0.25ml to 2l in any color or colorless. We have many bottle designs available for a variety of industries and applications.</p>
  <span class="more">READ MORE <i></i></span>
</div>

<!-- testimonials -->
<section class="abs testi">
  <h2 class="abs">Our Testimonials</h2>
  <p class="abs lead">Lorem ipsum dolor sit amet, consectetur adipiscing elit, sed do eiusmod tempor incididunt ut labore et dolore magna aliqua. enim ad minim veniam quis nostrud exercitation ullamco laboris nisi ut aliquip commodo consequat.</p>
  <div class="abs quote-card" style="left:110px"><p>"Lorem ipsum dolor sited consectetured adipiscing elited sed do eiusmod tempor incididunt uted labore eted dolore sed magna aliqua enim ad minim veniam,</p><div class="who"><div class="avatar" role="img" aria-label="Customer portrait"></div><div><b>Jonas Berger</b><span class="stars">★★★★★</span></div><span class="mark">”</span></div></div>
  <div class="abs quote-card" style="left:443px"><p>"Lorem ipsum dolor sited consectetured adipiscing elited sed do eiusmod tempor incididunt uted labore eted dolore sed magna aliqua enim ad minim veniam,</p><div class="who"><div class="avatar" role="img" aria-label="Customer portrait"></div><div><b>Jonas Berger</b><span class="stars">★★★★★</span></div><span class="mark">”</span></div></div>
  <div class="abs quote-card" style="left:775px"><p>"Lorem ipsum dolor sited consectetured adipiscing elited sed do eiusmod tempor incididunt uted labore eted dolore sed magna aliqua enim ad minim veniam,</p><div class="who"><div class="avatar" role="img" aria-label="Customer portrait"></div><div><b>Jonas Berger</b><span class="stars">★★★★★</span></div><span class="mark">”</span></div></div>
</section>

<!-- gallery -->
<h2 class="abs sec-title" style="top:3221px">Our <span class="accent">Gallery</span></h2>
<div class="abs tile" style="left:125px;top:3303px;width:305px;height:394px;background:linear-gradient(170deg,#6f8a4a,#8f8570 55%,#b9b3a7)" role="img" aria-label="Cyclist standing beside a cargo bike holding a parcel"></div>
<div class="abs tile" style="left:446px;top:3303px;width:306px;height:190px;background:linear-gradient(160deg,#8a8f95,#a7a29a 50%,#6b6a60)" role="img" aria-label="Rider on a cargo bike with a box in the city"></div>
<div class="abs tile" style="left:446px;top:3506px;width:306px;height:191px;background:linear-gradient(160deg,#8b5a45,#c0522e 45%,#7c7a75)" role="img" aria-label="Red box cargo bike parked by a brick wall"></div>
<div class="abs tile" style="left:770px;top:3303px;width:305px;height:394px;background:linear-gradient(170deg,#4d5a3d,#7b7a66 50%,#b8b5aa)" role="img" aria-label="Courier riding a yellow cargo bike on a crossing"></div>

<!-- footer -->
<footer class="abs footer">
  <svg class="abs" style="left:0;top:0" width="1200" height="491" viewBox="0 0 1200 491">
    <path d="M0 150 C300 20 850 20 1200 150 L1200 491 L0 491Z" fill="#141414"/>
    <path d="M0 150 C300 20 850 20 1200 150" fill="none" stroke="#f47a20" stroke-width="5"/>
  </svg>
  <div class="abs brandf">Veloria Kastwerk</div>
  <p class="abs about-f">Lorem ipsum dolor sit amet consectetur adipiscing elit sed do eiusmod tempor incididunt uted labore eted dolor.</p>
  <div class="abs social" aria-label="Social links"><span></span><span></span><span></span><span></span></div>
  <div class="abs" style="left:463px;top:148px"><h5>Quick Links</h5><ul><li>Home</li><li>About Us</li><li>Products</li><li>Services</li><li>Blog</li><li>Contact us</li></ul></div>
  <div class="abs" style="left:658px;top:148px"><h5>About Company</h5><ul><li>Terms of Use</li><li>Terms &amp; Condition</li><li>News</li><li>Privacy Policy</li><li>FAQ</li></ul></div>
  <div class="abs" style="left:880px;top:148px;width:210px"><h5>Contact Us</h5>
    <div class="ci"><svg width="12" height="16" viewBox="0 0 12 16"><path d="M6 0a6 6 0 0 1 6 6c0 4-6 10-6 10S0 10 0 6a6 6 0 0 1 6-6z" fill="#f47a20"/><circle cx="6" cy="6" r="2.2" fill="#141414"/></svg><div><small>Location</small><span>283, Lorem ipsum dolrmeted consectetur adipiscing elited</span></div></div>
    <div class="ci"><svg width="14" height="14" viewBox="0 0 24 24"><path d="M6.6 10.8c1.4 2.8 3.8 5.1 6.6 6.6l2.2-2.2c.3-.3.7-.4 1-.2 1.1.4 2.3.6 3.6.6.6 0 1 .4 1 1V20c0 .6-.4 1-1 1C10.6 21 3 13.4 3 4c0-.6.4-1 1-1h3.5c.6 0 1 .4 1 1 0 1.3.2 2.5.6 3.6.1.3 0 .7-.2 1z" fill="#f47a20"/></svg><div><small>Phone</small><span>+1 555 014 2299</span></div></div>
    <div class="ci"><svg width="14" height="12" viewBox="0 0 14 12"><rect x="0" y="1" width="14" height="10" fill="#f47a20"/><path d="M0 1l7 5 7-5" stroke="#141414" stroke-width="1.4" fill="none"/></svg><div><small>Email</small><span>info@veloriakastwerk.com</span></div></div>
  </div>
  <div class="abs up"><svg width="14" height="10" viewBox="0 0 14 10"><path d="M2 8l5-5 5 5" stroke="#fff" stroke-width="2.2" fill="none"/></svg></div>
  <div class="abs rule"></div>
  <div class="abs copy">2021 Copyright - Veloria Kastwerk | All Rights Reserved</div>
</footer>

</body>
</html>
```